I need a CD cover (simple single CD -- NOT jewel case) for my new CD. This is a very small independent project -- probably 100 - 200 copies to be made in total. The name of the CD is "Folded Lanterns". My name (artist) is vel marsh (I prefer lower case for my name). I just want an interesting design on the front cover that has both the CD name and my name (no photo) -- just something that looks cool -- I'm open to any and all ideas. The back should contain the enclosed photo -- I am open to the photo being any size -- even very small if that looks best. The front cover design will also need to be ON the CD itself (adapted as needed). I am not concerned with the design of the front having any relationship to the music -- I just want something that is attractive and looks cool.
Look and feel
Each slider illustrates characteristics of the customer's brand and the style your logo design should communicate.

```html
<!DOCTYPE html>
<html lang="en">
<head>
<meta charset="utf-8">
<title>Folded Lanterns — vel marsh</title>
<link rel="stylesheet" href="https://fonts.googleapis.com/css2?family=PT+Sans+Narrow:wght@700&family=Cormorant+Garamond:ital,wght@1,400&display=swap">
<style>
  :root {
    --night: #07050a;
    --deep-plum: #2a0d24;
    --magenta-glow: #7a2a78;
    --orchid-core: #b77fc4;
    --teal-haze: #17303a;
    --title-pink: #ff0a78;
    --name-white: #f4f1f4;
  }
  html, body {
    margin: 0;
    padding: 0;
    width: 1200px;
    height: 1200px;
    overflow: hidden;
    background: var(--night);
  }
  .cover {
    position: relative;
    width: 1200px;
    height: 1200px;
    overflow: hidden;
    background: var(--night);
  }
  .cover-artwork {
    position: absolute;
    inset: 0;
    background:
      radial-gradient(ellipse 26% 30% at 52% 52%, var(--orchid-core) 0%, rgba(183,127,196,0.55) 35%, rgba(122,42,120,0) 100%),
      radial-gradient(ellipse 62% 30% at 50% 55%, rgba(122,42,120,0.55) 0%, rgba(42,13,36,0.35) 60%, rgba(7,5,10,0) 100%),
      radial-gradient(ellipse 40% 30% at 15% 10%, rgba(122,30,80,0.45) 0%, rgba(7,5,10,0) 100%),
      radial-gradient(ellipse 45% 35% at 85% 85%, rgba(23,48,58,0.6) 0%, rgba(7,5,10,0) 100%),
      linear-gradient(160deg, var(--deep-plum) 0%, var(--night) 45%, var(--night) 70%, var(--teal-haze) 100%);
  }
  .album-title {
    position: absolute;
    right: 54px;
    top: 1030px;
    margin: 0;
    font-family: "PT Sans Narrow", "Arial Narrow", sans-serif;
    font-weight: 700;
    font-size: 63px;
    line-height: 1;
    letter-spacing: 0.5px;
    text-transform: uppercase;
    color: var(--title-pink);
    white-space: nowrap;
  }
  .artist-name {
    position: absolute;
    right: 138px;
    top: 1082px;
    margin: 0;
    font-family: "Cormorant Garamond", "Georgia", serif;
    font-style: italic;
    font-weight: 400;
    font-size: 74px;
    line-height: 1;
    letter-spacing: 0.24em;
    color: var(--name-white);
    white-space: nowrap;
  }
</style>
</head>
<body>
  <main class="cover">
    <div class="cover-artwork" role="img" aria-label="Abstract fractal artwork: glowing pink and violet swirling loops at the centre, sweeping magenta light ribbons and a web of fine pale lines with small translucent squares on a black background"></div>
    <h1 class="album-title">Folded Lanterns</h1>
    <p class="artist-name">vel marsh</p>
  </main>
</body>
</html>
```